Boutique winery needs new wine label

domaine Verlin is a boutique wine company based in the Clare Valley of South Australia. We are an established brand, best known for our Riesling and Grenache. We plan to launch a new sub brand called La Douce ferme and require a new label that is different from the others we use. It will be used on small batch Riesling and should have a rustic but quality feel. Attached is a small image of the house where the winery is based. The label should incorporate a hand drawn sketch of the house.
Target Market(s)
High end wine consumers with an interest in Riesling
Requirements
Must have
- hand drawn sketch of the house
- the name of the wine La Douce ferme present on the front label
- Vintage (2018) and region (Clare Valley) present on the front label
- Minimal use of colour on the label but would look at embellishments such as gold foil
Nice to have
- A clean, simple style of label, preferably with white background
- La Douce ferme written in script style
Should not have
- domaine Verlin written on the front label
- the current domaine Verlin logo

```html
<!DOCTYPE html>
<html lang="en">
<head>
<meta charset="utf-8">
<title>La Douce ferme – Vintage 2018 Label</title>
<link rel="stylesheet" href="https://fonts.googleapis.com/css2?family=Felipa&family=Amita:wght@400&display=swap">
<style>
  :root {
    --page: #ffffff;
    --label-black: #0b0b0b;
    --gold-light: #fbe88f;
    --gold-mid: #f2c94c;
    --gold-deep: #c98a2b;
    --gold-bronze: #b87333;
    --gold-foil: linear-gradient(90deg, #d9a23a 0%, #f7d66a 22%, #b87a2e 45%, #f9e38e 70%, #d59a34 100%);
    --gold-text: linear-gradient(180deg, #fff2a8 0%, #f4cd55 45%, #d79a2c 100%);
  }
  * { margin: 0; padding: 0; box-sizing: border-box; }
  html, body {
    width: 1134px;
    height: 1200px;
    overflow: hidden;
    background: var(--page);
  }
  .canvas {
    position: relative;
    width: 1134px;
    height: 1200px;
  }
  .label {
    position: absolute;
    left: 120px;
    top: 125px;
    width: 873px;
    height: 910px;
    background: var(--gold-foil);
    padding: 12px;
  }
  .label__panel {
    position: relative;
    width: 100%;
    height: 100%;
    background: var(--label-black);
  }
  .label__title {
    position: absolute;
    left: 0;
    right: 0;
    top: 78px;
    text-align: center;
    font-family: "Felipa", cursive;
    font-size: 104px;
    line-height: 1;
    background: var(--gold-text);
    -webkit-background-clip: text;
    background-clip: text;
    color: transparent;
  }
  .label__house {
    position: absolute;
    left: 161px;
    top: 256px;
    width: 527px;
    height: 329px;
    background: var(--gold-foil);
    padding: 5px;
  }
  .label__house-art {
    width: 100%;
    height: 100%;
    background:
      linear-gradient(180deg, rgba(0,0,0,0) 0%, rgba(0,0,0,0) 28%, rgba(90,90,90,0.55) 40%, rgba(70,75,70,0.9) 100%),
      linear-gradient(90deg, #f1c74f 0%, #fbe99a 50%, #f1c74f 100%);
  }
  .label__details {
    position: absolute;
    left: 0;
    right: 0;
    top: 686px;
    text-align: center;
    font-family: "Amita", serif;
    font-size: 49px;
    letter-spacing: 3px;
    line-height: 87px;
    color: var(--gold-mid);
  }
  .label__details span {
    display: block;
    background: var(--gold-text);
    -webkit-background-clip: text;
    background-clip: text;
    color: transparent;
  }
</style>
</head>
<body>
  <main class="canvas">
    <section class="label">
      <div class="label__panel">
        <h1 class="label__title">La Douce ferme</h1>
        <div class="label__house">
          <div class="label__house-art" role="img" aria-label="Hand drawn sketch of the two-storey stone winery house with shuttered windows, a small balcony and climbing vines, set on a gold foil background"></div>
        </div>
        <p class="label__details">
          <span class="label__vintage">Vintage 2018</span>
          <span class="label__region">Clare Valley</span>
        </p>
      </div>
    </section>
  </main>
</body>
</html>
```